Industrial/Commercial Plumbing Capability Statement

Would like a construction capability statement/Brochure amended to be similar to the attached. -
Have included photos and Notes on the attached
would like project photos to be used
This is a previous capability statement that we would like amended and altered to include, safety, QA and Recent Projects
Please use our company logo
Updates

Need extra days to review

Target Market(s)

Construction work - Industrial

Industry/Entity Type

Plumbing

Requirements
Must have
• Include all items in contents page

Eye Catching Photos relevant to construction industry and relevant to topic on page

```html
<!DOCTYPE html>
<html lang="en">
<head>
<meta charset="utf-8">
<title>Kestrel Plumbers – Capability Statement</title>
<link rel="stylesheet" href="https://fonts.googleapis.com/css2?family=Rubik:wght@400;500;700;800&display=swap">
<style>
  :root {
    --stage: #2a2a2c;
    --rule: #6a6a6c;
    --navy: #123a63;
    --navy-deep: #0d2c4d;
    --navy-light: #1f5482;
    --white: #ffffff;
    --muted: #c9d6e4;
    --sky-top: #6f86b4;
    --sky-mid: #c7a9a2;
    --sky-glow: #ef9a5c;
    --skyline: #5b5f6a;
    --grass: #3f5a2c;
  }
  * { margin: 0; padding: 0; box-sizing: border-box; }
  html, body { width: 913px; height: 1200px; overflow: hidden; }
  body {
    background: var(--stage);
    font-family: "Rubik", sans-serif;
    color: var(--white);
    position: relative;
  }
  .spread {
    position: absolute;
    left: 116px;
    width: 680px;
    height: 480px;
    display: flex;
    box-shadow: 0 12px 30px rgba(0,0,0,.5);
  }
  .spread--covers { top: 56px; }
  .spread--inside { top: 654px; }
  .divider {
    position: absolute;
    left: 0; right: 0; top: 598px;
    height: 1px;
    background: var(--rule);
  }
  .page {
    position: relative;
    width: 340px;
    height: 480px;
    overflow: hidden;
  }
  .section-title {
    font-weight: 800;
    text-transform: uppercase;
    line-height: 1.05;
    border-left: 2px solid var(--white);
    padding-left: 8px;
    letter-spacing: .5px;
  }
  .brand {
    display: flex;
    align-items: center;
    gap: 6px;
    font-weight: 800;
    text-transform: uppercase;
    letter-spacing: .5px;
    white-space: nowrap;
  }
  .brand-square {
    width: 14px; height: 14px;
    background: currentColor;
  }

  /* Back cover */
  .back-cover { background: var(--navy); }
  .back-cover .city-fade {
    position: absolute; left: 0; right: 0; bottom: 0; height: 320px;
    background: linear-gradient(180deg, rgba(18,58,99,0) 0%, rgba(40,80,120,.45) 45%, rgba(13,44,77,.6) 100%);
  }
  .back-cover .brand {
    position: absolute; left: 50%; top: 240px;
    transform: translate(-50%, -50%);
    font-size: 20px;
  }

  /* Front cover */
  .front-cover .cover-photo {
    position: absolute; inset: 0;
    background: linear-gradient(180deg, var(--sky-top) 0%, #9aa7c8 25%, var(--sky-mid) 42%, var(--sky-glow) 55%, var(--skyline) 70%, var(--grass) 88%, #2f4421 100%);
  }
  .front-cover .section-title {
    position: absolute; left: 34px; top: 40px;
    font-size: 20px;
  }
  .front-cover .brand {
    position: absolute; right: 22px; bottom: 22px;
    font-size: 14px;
    color: var(--navy);
    background: var(--white);
    padding: 4px 8px;
  }

  /* Contents */
  .contents-page {
    background: linear-gradient(160deg, var(--navy) 0%, var(--navy-deep) 100%);
    padding: 40px 34px;
  }
  .contents-page .section-title { font-size: 22px; }
  .contents-list {
    list-style: none;
    margin-top: 70px;
  }
  .contents-list li {
    display: flex;
    align-items: baseline;
    font-size: 9.5px;
    font-weight: 700;
    text-transform: uppercase;
    line-height: 2;
  }
  .contents-list .leader {
    flex: 1;
    border-bottom: 1px dotted var(--white);
    margin: 0 4px;
    transform: translateY(-3px);
  }
  .contents-page .brand {
    position: absolute; left: 34px; bottom: 40px;
    font-size: 16px;
  }

  /* Introduction */
  .intro-page {
    background: linear-gradient(200deg, var(--navy-light) 0%, var(--navy) 60%, var(--navy-deep) 100%);
    padding: 40px 30px;
  }
  .intro-page .section-title { font-size: 22px; }
  .intro-body { margin-top: 28px; }
  .intro-body p {
    font-size: 7px;
    line-height: 1.5;
    color: var(--muted);
    margin-bottom: 9px;
  }
  .intro-highlight {
    background: var(--white);
    color: var(--navy);
    font-size: 10px;
    font-weight: 500;
    line-height: 1.35;
    padding: 7px 10px;
    margin: 12px -6px 14px;
  }
  .intro-page .brand {
    position: absolute; right: 30px; bottom: 32px;
    font-size: 16px;
  }
</style>
</head>
<body>
  <section class="spread spread--covers">
    <article class="page back-cover">
      <div class="city-fade" role="img" aria-label="Faint navy-tinted city skyline photograph"></div>
      <div class="brand"><span class="brand-square"></span>Kestrel Plumbers.</div>
    </article>
    <article class="page front-cover">
      <div class="cover-photo" role="img" aria-label="City skyline at sunset seen from a green hillside"></div>
      <h1 class="section-title">Capability<br>Statement</h1>
      <div class="brand"><span class="brand-square"></span>Kestrel Plumbers.</div>
    </article>
  </section>

  <div class="divider"></div>

  <section class="spread spread--inside">
    <article class="page contents-page">
      <h2 class="section-title">Table of<br>Contents</h2>
      <ul class="contents-list">
        <li>From the Directors<span class="leader"></span>3</li>
        <li>About the Business<span class="leader"></span>4</li>
        <li>Our Services<span class="leader"></span>6</li>
        <li>KP Data<span class="leader"></span>7</li>
        <li>Meet the Team<span class="leader"></span>8</li>
        <li>Recent Projects<span class="leader"></span>9</li>
        <li>KP Data<span class="leader"></span>10</li>
        <li>Meet the Team<span class="leader"></span>12</li>
      </ul>
      <div class="brand"><span class="brand-square"></span>Kestrel Plumbers.</div>
    </article>
    <article class="page intro-page">
      <h2 class="section-title">Introduction</h2>
      <div class="intro-body">
        <p>Our modern approach to plumbing construction means your project benefits from the latest materials, techniques and industry developments, delivered by a trusted team on every site.</p>
        <p>Our innovative and dynamic approach keeps us ahead, and we work closely with builders on the scope of works to guarantee that expectations are met and exceeded.</p>
        <div class="intro-highlight">Kestrel Plumbers having extensive expertise across many areas, from new Shopping centres and Hospitals to industrial equipment.</div>
        <p>We constantly strive to exceed the expectations of our customers and have a proven track record with the delivery of large scale projects, on time and on budget.</p>
        <p>We pride ourselves on quality on-site management, clear communication and effective collaboration, and we stand steadfast in our reputation as reliable problem solvers.</p>
        <p>Kestrel Plumbers believe that with the proper team you can avoid costly and unnecessary delays. When you work with us you are dealing with trusted commercial specialists.</p>
        <p>We can't wait to start working with you.</p>
      </div>
      <div class="brand"><span class="brand-square"></span>Kestrel Plumbers.</div>
    </article>
  </section>
</body>
</html>
```